Tech + Media Consulting Business // LOGO + Card

We need a logo design and business card for a Seattle-area strategy consulting firm. We believe in big, expansive thinking and we work for tech/media startups, as well as big companies like Vantrel and Quillo. We would like designs inspired by the mountains and skies of Montana and Colorado. Existing logo attached but we would like a fresh approach.

Target Market(s)

Technology and Media Executives

Industry/Entity Type

Information Technology

Contact Information for Business Card

Martin Ollery
2715 61st Avenue NE
Orwick WA 98052
Phone: 206-471-9253
martinollery@tidefernadvisory.biz

Logo Text

Tidefern Advisory LLC

Font styles to use
Sans Serif

Colors

Designer to choose colors to be used in the design.

Requirements
Must have
• Logo inspired by mountains and sky.
• Our company wants to inspire our clients to think expansively -- embracing exploration and new ideas.
Nice to have
• Colors inspired by Larchwood-brand.
• We don't have a website at present but would like a field to add one later. Until then, we may reference our LinkedIn page:
• https://www.example-profiles.net/company/tidefern-advisory-llc-nw

```html
<!DOCTYPE html>
<html lang="en">
<head>
<meta charset="utf-8">
<title>Tidefern Advisory LLC — Business Card</title>
<link rel="stylesheet" href="https://fonts.googleapis.com/css2?family=Montserrat:wght@400;500;700&family=Roboto:wght@400;500&display=swap">
<style>
  :root {
    --stage: #2b2b2d;
    --card: #ffffff;
    --ink: #111111;
    --navy: #2e2a86;
    --rule: #222222;
  }
  * { margin: 0; padding: 0; box-sizing: border-box; }
  html, body { width: 1200px; height: 905px; overflow: hidden; }
  body {
    background: var(--stage);
    display: flex;
    flex-direction: column;
    align-items: center;
    justify-content: center;
    gap: 56px;
    font-family: "Roboto", Arial, sans-serif;
  }
  .card {
    width: 620px;
    height: 354px;
    background: var(--card);
    border-radius: 28px;
    position: relative;
    box-shadow: 0 10px 30px rgba(0,0,0,0.45);
  }
  .brand {
    display: flex;
    align-items: center;
    gap: 14px;
  }
  .brand-dot {
    width: 46px;
    height: 46px;
    border-radius: 50%;
    background: var(--navy);
    flex: none;
  }
  .brand-name {
    font-family: "Montserrat", Arial, sans-serif;
    font-weight: 700;
    color: var(--navy);
    font-size: 22px;
    line-height: 1.1;
    letter-spacing: 0.5px;
    text-transform: uppercase;
  }
  .card-front {
    display: flex;
    align-items: center;
    justify-content: center;
  }
  .card-front .brand-dot { width: 60px; height: 60px; }
  .card-front .brand-name { font-size: 28px; }

  .card-back {
    display: flex;
    align-items: center;
    padding: 0 40px 0 44px;
  }
  .card-back .brand { width: 220px; }
  .card-back .brand-name { font-size: 18px; }
  .divider {
    width: 1.5px;
    height: 180px;
    background: var(--rule);
    margin: 0 26px 0 18px;
    flex: none;
  }
  .details { color: var(--ink); }
  .person {
    font-family: "Montserrat", Arial, sans-serif;
    font-size: 30px;
    line-height: 1;
    margin-bottom: 8px;
    text-transform: uppercase;
    white-space: nowrap;
  }
  .person-first { font-weight: 700; color: var(--ink); }
  .person-last { font-weight: 400; color: var(--navy); }
  .address {
    font-size: 14px;
    line-height: 1.35;
    margin-bottom: 14px;
    font-style: normal;
  }
  .contact-list { list-style: none; }
  .contact-item {
    display: flex;
    align-items: center;
    gap: 10px;
    font-size: 14px;
    line-height: 1;
    margin-bottom: 7px;
    white-space: nowrap;
  }
  .contact-icon {
    width: 20px;
    height: 20px;
    border-radius: 50%;
    background: var(--navy);
    display: flex;
    align-items: center;
    justify-content: center;
    flex: none;
  }
</style>
</head>
<body>

  <section class="card card-front" aria-label="Card front">
    <div class="brand">
      <span class="brand-dot"></span>
      <span class="brand-name">Tidefern<br>Advisory LLC</span>
    </div>
  </section>

  <section class="card card-back" aria-label="Card back">
    <div class="brand">
      <span class="brand-dot"></span>
      <span class="brand-name">Tidefern<br>Advisory LLC</span>
    </div>
    <span class="divider"></span>
    <div class="details">
      <h1 class="person"><span class="person-first">Martin</span> <span class="person-last">Ollery</span></h1>
      <address class="address">2715 61st Avenue NE<br>Orwick WA 98052</address>
      <ul class="contact-list">
        <li class="contact-item">
          <span class="contact-icon">
            <svg width="11" height="11" viewBox="0 0 24 24" aria-hidden="true"><path fill="#fff" d="M6.6 10.8a15.1 15.1 0 0 0 6.6 6.6l2.2-2.2c.3-.3.7-.4 1-.2 1.1.4 2.3.6 3.6.6.6 0 1 .4 1 1V20c0 .6-.4 1-1 1A17 17 0 0 1 3 4c0-.6.4-1 1-1h3.5c.6 0 1 .4 1 1 0 1.3.2 2.5.6 3.6.1.3 0 .7-.2 1z"/></svg>
          </span>
          206-471-9253
        </li>
        <li class="contact-item">
          <span class="contact-icon">
            <svg width="12" height="10" viewBox="0 0 24 18" aria-hidden="true"><rect x="1" y="1" width="22" height="16" rx="2" fill="none" stroke="#fff" stroke-width="2.2"/><path d="M2 2l10 8 10-8" fill="none" stroke="#fff" stroke-width="2.2"/></svg>
          </span>
          martinollery@tidefernadvisory.biz
        </li>
        <li class="contact-item">
          <span class="contact-icon"></span>
          www.example-profiles.net/company/tidefern-biz
        </li>
      </ul>
    </div>
  </section>

</body>
</html>
```